Lift Your Revenue 100% In Warm Offers 2013 With The Kestrel Circle

Please vist www.brimwellhub.com, use all the images of the current advertisers there on the Home page and create a better flyer from this attached old flyer.

Industry/Entity Type

Sales

```html
<!DOCTYPE html>
<html lang="en">
<head>
<meta charset="utf-8">
<title>Warm Offers 2013 — The Kestrel Circle</title>
<link rel="stylesheet" href="https://fonts.googleapis.com/css2?family=Archivo+Black&family=Arimo:wght@400;700&display=swap">
<style>
  :root {
    --red: #ee1c24;
    --red-light: #f5434a;
    --red-deep: #d8141b;
    --ink: #111111;
    --paper: #ffffff;
  }
  * { margin: 0; padding: 0; box-sizing: border-box; }
  html, body { width: 927px; height: 1200px; overflow: hidden; background: var(--paper); }
  .flyer { position: relative; width: 927px; height: 1200px; overflow: hidden; background: var(--paper); font-family: "Arimo", Arial, sans-serif; color: var(--ink); }
  .layer { position: absolute; inset: 0; }
  .headline text { font-family: "Archivo Black", "Arial Black", sans-serif; }
  .copy text { font-family: "Arimo", Arial, sans-serif; fill: var(--ink); }
  .copy .bold { font-weight: 700; }
  .lead-line { font-size: 58px; }
  .boost-line { font-size: 62px; }
  .pitch { font-size: 32px; }
  .promise__guarantee { font-size: 24px; }
  .promise__sponsor { font-size: 29px; }
  .promise__card { font-size: 24px; }
  .footer { font-size: 18px; }
  .showcase { position: absolute; border: 2px solid var(--paper); box-shadow: 0 1px 4px rgba(0,0,0,.35); }
  .showcase--denim { left: 22px; top: 562px; width: 296px; height: 170px; transform: rotate(1.5deg); background: linear-gradient(135deg, #2c3d5c, #5a6f92 55%, #273650); }
  .showcase--software { left: 343px; top: 590px; width: 270px; height: 148px; transform: rotate(1.2deg); background: linear-gradient(120deg, #f4f6f8 40%, #3a8fd6 70%, #1b1b1b); }
  .showcase--beauty { left: 640px; top: 568px; width: 258px; height: 134px; transform: rotate(1.5deg); background: linear-gradient(90deg, #f2f2f2 40%, #e6784a 70%, #d9c3b1); }
  .showcase--coffee { left: 42px; top: 758px; width: 250px; height: 130px; transform: rotate(1deg); background: linear-gradient(90deg, #e8e8e4, #8a7a6a 55%, #4a3124); }
  .showcase--coins { left: 305px; top: 743px; width: 266px; height: 146px; transform: rotate(-2deg); background: linear-gradient(100deg, #f0eee8 30%, #c9a64a 65%, #8c6b1f); }
  .showcase--retail { left: 614px; top: 724px; width: 284px; height: 166px; transform: rotate(-1.5deg); background: linear-gradient(160deg, #2b6cc4, #6ea4e0 45%, #e6e0e8); }
</style>
</head>
<body>
<main class="flyer">
  <svg class="layer" width="927" height="1200" viewBox="0 0 927 1200" aria-hidden="true">
    <path d="M0 578 C 300 690, 600 820, 927 900 L927 1200 L0 1200 Z" fill="var(--red)"/>
    <path d="M0 578 C 300 690, 600 820, 927 900 L927 830 C 600 760, 300 640, 0 540 Z" fill="var(--red-light)"/>
    <path d="M0 640 C 300 760, 600 870, 927 930 L927 1200 L0 1200 Z" fill="var(--red-deep)" opacity=".35"/>
  </svg>

  <svg class="layer headline" width="927" height="1200" viewBox="0 0 927 1200">
    <g font-size="128" text-anchor="middle">
      <text x="463" y="232" textLength="890" lengthAdjust="spacingAndGlyphs" fill="var(--red)" stroke="var(--red)" stroke-width="12" stroke-linejoin="round">WARM OFFERS</text>
      <text x="463" y="232" textLength="890" lengthAdjust="spacingAndGlyphs" fill="var(--red)" stroke="var(--paper)" stroke-width="5" stroke-linejoin="round">WARM OFFERS</text>
      <text x="463" y="232" textLength="890" lengthAdjust="spacingAndGlyphs" fill="var(--red)">WARM OFFERS</text>
    </g>
    <g font-size="160" text-anchor="middle">
      <text x="463" y="392" textLength="820" lengthAdjust="spacing" fill="var(--red)" stroke="var(--red)" stroke-width="12" stroke-linejoin="round">2013</text>
      <text x="463" y="392" textLength="820" lengthAdjust="spacing" fill="var(--red)" stroke="var(--paper)" stroke-width="5" stroke-linejoin="round">2013</text>
      <text x="463" y="392" textLength="820" lengthAdjust="spacing" fill="var(--red)">2013</text>
    </g>
  </svg>

  <div class="showcase showcase--denim" role="img" aria-label="Photo of denim jeans from an advertiser"></div>
  <div class="showcase showcase--software" role="img" aria-label="Photo of software boxes and a game console from an advertiser"></div>
  <div class="showcase showcase--beauty" role="img" aria-label="Photo of cosmetics and skincare products from an advertiser"></div>
  <div class="showcase showcase--coffee" role="img" aria-label="Photo of coffee packaging and desserts from an advertiser"></div>
  <div class="showcase showcase--coins" role="img" aria-label="Photo of collectible silver and gold coins from an advertiser"></div>
  <div class="showcase showcase--retail" role="img" aria-label="Photo of phones, electronics and makeup from a retail advertiser"></div>

  <svg class="layer copy" width="927" height="1200" viewBox="0 0 927 1200">
    <text class="lead-line bold" x="16" y="96" textLength="895" lengthAdjust="spacingAndGlyphs">If you join the Kestrel Circle now for</text>
    <text class="boost-line bold" x="10" y="456" textLength="908" lengthAdjust="spacingAndGlyphs">We boost your sales up to 100%</text>
    <text class="pitch" x="136" y="522" textLength="656" lengthAdjust="spacingAndGlyphs">Stop offering “?%off” discounts,</text>
    <text class="pitch" x="68" y="553" textLength="802" lengthAdjust="spacingAndGlyphs">and start making much <tspan class="bold">MORE</tspan> money!</text>
    <text class="promise__guarantee bold" x="60" y="930" textLength="810" lengthAdjust="spacingAndGlyphs">We guarantee you make more money with our program,</text>
    <text class="promise__guarantee bold" x="323" y="955" textLength="302" lengthAdjust="spacingAndGlyphs">or your money back!</text>
    <text class="promise__sponsor bold" x="95" y="993" textLength="730" lengthAdjust="spacingAndGlyphs">This hot deal summer promotion is sponsered</text>
    <text class="promise__sponsor bold" x="120" y="1021" textLength="678" lengthAdjust="spacingAndGlyphs">by our business entities and Brimwell Hub.</text>
    <text class="promise__card bold" x="18" y="1080" textLength="887" lengthAdjust="spacingAndGlyphs">Shop, save, and get bonuses with our Brimwell Northbank Debit Card!</text>
    <text class="footer" x="450" y="1178" textLength="455" lengthAdjust="spacingAndGlyphs">All Rights Reserved. 2013 BrimwellHub.com</text>
  </svg>
</main>
</body>
</html>
```